Corvastin Office Solutions needs a new interactive and interesting website

We need an interesting, professional, modern and functional company website for Corvastin Office Solutions - a young IT Services company based out of Chennai, India.

Corvastin Office Solutions is a fully owned subsidiary of Hollin Cellarhouse, one of the world's leading direct to consumer wine merchant.

We already have a registered company logo which must feature in the website.

We conceive, design, develop, test, implement and support IT solutions across the entire Hollin Cellarhouse IT landscape. For ex : We currently run about 25 e-commerce websites for Hollin Cellarhouse on QVM and Dot Net.

We would like to see our corporate colors used in the website. (Burgundy wine and wine green - source: www.corvastinos.example)

We are looking at this website to communicate a fun, friendly and professionally managed company - reaching out to career seekers, prospective customers and general public.

For reference - The company name 'Corvastin' is an inspiration from the Hollin Cellarhouse lineage.

The second image with the world map is stickered on our main entrance to the office, I am not sure where this can be used -just putting it out there..
Updates

Please note that there are only a few more days to submit designs for this contest  !

I would appreciate if you can help posting your designs in time for our review and consideration.

Thanks.

Project Deadline Extended
Reason: Thanks for your inputs. We have a number of designers and a lot to digest and work with in the past few days. There has been a rush of new designs in the last few days Hence we will require more time to process these and make our decision. Hence i am requesting the contest to be open for more days. Regards, Soren

Target Market(s)

Prospective job seekers who want to know more about the company and also wish to apply for a job vacancy
People wanting to know more about the company in general and our progress
People who want to see what we offer and how we can help them too - prospective customers
Companies that are interested in our IT Captive journey and are looking for a business opportunity

Industry/Entity Type

E-Commerce

Requirements
Must have
• Log In/ Register facility acting as a Single Sign on for Intranet (Employees)

Facility to post job vacancies (with an expiry date) and enable people to apply for a role and upload their CV/Resume.

Facility to Review Job applications

Facility for website visitors to contact Tallowmere office Solutions via an online 'Contact Us' form with a split of job seekers and business opportunities

Gallery facility to upload pictures regarding company events
Nice to have
• Less Cluttered and contemporary design
Some Wine/Vineyard inspirations will be good but not too much, the company is an IT services company

```html
<!DOCTYPE html>
<html lang="en">
<head>
<meta charset="utf-8">
<title>Corvastin Office Solutions</title>
<link href="https://fonts.googleapis.com/css2?family=Varela+Round&family=Montserrat:wght@400;500;600&family=Open+Sans:wght@400;600&display=swap" rel="stylesheet">
<style>
:root{
  --burgundy:#8a003f;
  --burgundy-dark:#6c0033;
  --burgundy-deep:#5a002a;
  --hero-light:#a8145a;
  --grey-light:#e4e2e3;
  --grey-mid:#cfcdce;
  --grey-line:#b9b7b8;
  --text:#222;
  --text-soft:#444;
  --white:#fff;
}
*{box-sizing:border-box;margin:0;padding:0}
html,body{width:1090px;height:1200px;overflow:hidden}
body{font-family:"Open Sans",Arial,sans-serif;color:var(--text);background:var(--white);position:relative}
a{color:inherit;text-decoration:none}

/* header */
.site-header{position:absolute;left:0;top:0;width:1090px;height:114px;background:var(--burgundy)}
.brand{position:absolute;left:60px;top:40px;display:flex;align-items:center;gap:10px;color:var(--white);font-family:"Varela Round",sans-serif}
.brand-dot{width:26px;height:26px;border-radius:50%;background:var(--white)}
.brand-name{font-size:31px;line-height:30px}
.brand-sub{font-size:19px;line-height:22px}
.login-form{position:absolute;top:62px;left:545px;display:flex;align-items:center}
.login-field{width:144px;height:26px;background:var(--grey-light);border:0;font-family:"Montserrat",sans-serif;font-size:13px;color:#bdbbbc;padding:0 11px;line-height:26px;margin-right:12px}
.login-btn{margin-left:15px;width:77px;height:32px;background:var(--burgundy-dark);color:var(--white);font-family:"Montserrat",sans-serif;font-weight:500;font-size:16px;text-align:center;line-height:32px}
.register-link{margin-left:18px;color:var(--white);font-family:"Montserrat",sans-serif;font-weight:500;font-size:16px}

/* nav */
.main-nav{position:absolute;left:0;top:114px;width:1090px;height:49px;background:linear-gradient(#ebe9ea,#d4d2d3);box-shadow:0 2px 3px rgba(0,0,0,.25)}
.nav-links{position:absolute;left:63px;top:0;display:flex;list-style:none;font-family:"Montserrat",sans-serif;font-weight:500;font-size:14.5px;color:#333;line-height:49px}
.nav-links li{margin-right:47px}
.nav-actions{position:absolute;right:42px;top:13px;display:flex;gap:8px}
.pill-btn{height:24px;padding:0 13px;border-radius:12px;background:var(--burgundy-dark);color:var(--white);font-family:"Montserrat",sans-serif;font-weight:600;font-size:14px;line-height:24px}

/* hero */
.hero{position:absolute;left:0;top:163px;width:1090px;height:335px;background:radial-gradient(circle at 82% 45%,var(--hero-light) 0,var(--burgundy) 45%,var(--burgundy-deep) 100%)}
.hero-photo{position:absolute;left:48px;top:52px;width:385px;height:283px;background:linear-gradient(180deg,#c9b7bd 0%,#8f7682 60%,#5f4a56 100%);border-radius:120px 120px 0 0;opacity:.85}
.hero-copy{position:absolute;left:523px;top:72px;width:520px;color:var(--white);font-family:"Varela Round",sans-serif}
.hero-title{font-size:43px;font-weight:400;line-height:50px;margin-bottom:6px}
.hero-text{font-size:19px;line-height:26px;padding-left:3px;width:448px}
.hero-cta{position:absolute;left:523px;top:228px;width:172px;height:37px;background:linear-gradient(#f2f1f1,#c9c7c8);border:1px solid #999;display:flex;align-items:center;justify-content:space-between;padding:0 7px 0 18px;font-family:"Varela Round",sans-serif;font-size:19px;color:#333}

/* services */
.service-tabs{position:absolute;left:0;top:498px;width:1090px;height:79px;display:flex;background:linear-gradient(#e9e7e8,#d9d7d8);border-bottom:4px solid var(--grey-mid)}
.service-tab{display:flex;align-items:center;padding-left:20px;font-family:"Montserrat",sans-serif;font-weight:500;font-size:16px;line-height:19px;color:var(--text-soft);text-transform:uppercase;border-right:1px solid var(--grey-line)}
.service-tab:first-child{padding-left:49px}
.service-tab:last-child{border-right:0}

/* intro */
.intro{position:absolute;left:59px;top:605px;width:625px}
.intro-title{font-family:"Varela Round",sans-serif;font-weight:400;font-size:31px;color:var(--burgundy-dark);line-height:36px}
.intro-sub{font-family:"Varela Round",sans-serif;font-size:17px;color:var(--burgundy-dark);margin:3px 0 17px 2px}
.intro-text{font-size:12.5px;line-height:19px;letter-spacing:.3px;color:var(--text);margin-bottom:5px}

/* opportunities */
.opportunities{position:absolute;left:734px;top:606px;width:295px;height:294px;background:var(--grey-light);border-radius:3px}
.opportunities h2{font-family:"Varela Round",sans-serif;font-weight:400;font-size:20px;color:var(--burgundy-dark);padding:18px 0 0 12px;margin-bottom:15px}
.job{padding:0 8px 11px 12px;font-size:12.5px;letter-spacing:.6px;line-height:20px;color:#222}
.job + .job{border-top:1px solid var(--grey-line);padding-top:13px}
.job-more{text-align:right;color:var(--burgundy-dark);font-weight:600;letter-spacing:1px;margin-top:1px}

/* clients */
.clients{position:absolute;left:0;top:938px;width:1090px}
.clients h2{margin-left:60px;font-family:"Varela Round",sans-serif;font-weight:400;font-size:20px;color:var(--burgundy-dark)}
.client-row{position:absolute;left:0;top:60px;width:1090px;height:70px}
.arrow{position:absolute;top:2px}
.arrow-prev{left:58px}
.arrow-next{left:1022px;top:10px}
.client-name{position:absolute;top:12px;transform:translateX(-50%);font-family:"Varela Round",sans-serif;font-size:18px;color:var(--burgundy-dark);line-height:22px;white-space:nowrap}
.client-mark{display:inline-block;width:12px;height:12px;background:var(--burgundy-dark);margin-right:6px}

/* footer */
.site-footer{position:absolute;left:0;top:1094px;width:1090px;height:106px;background:var(--burgundy);color:var(--white)}
.footer-links{position:absolute;left:59px;top:22px;font-family:"Montserrat",sans-serif;font-weight:500;font-size:13.5px}
.footer-links span{margin:0 6px}
.social{position:absolute;left:59px;top:65px;display:flex;gap:22px}
.social-btn{display:flex;align-items:center;gap:5px}
.social-label{display:flex;align-items:center;gap:4px;height:21px;padding:0 5px;background:#3e5a93;border-radius:2px;font-family:"Montserrat",sans-serif;font-weight:600;font-size:11px;color:var(--white)}
.social-label i{display:inline-block;width:10px;height:10px;background:var(--white)}
.social-count{height:19px;padding:0 5px;background:var(--white);border:1px solid #bbb;border-radius:2px;font-size:11px;color:#333;line-height:17px}
.copyright{position:absolute;right:46px;top:74px;font-family:"Montserrat",sans-serif;font-size:11.5px}
</style>
</head>
<body>

<header class="site-header">
  <div class="brand">
    <span class="brand-dot"></span>
    <div>
      <div class="brand-name">corvastin</div>
      <div class="brand-sub">Office Solutions</div>
    </div>
  </div>
  <form class="login-form">
    <span class="login-field">Username</span>
    <span class="login-field">Password</span>
    <span class="login-btn">Login</span>
    <a class="register-link" href="#">Register</a>
  </form>
</header>

<nav class="main-nav">
  <ul class="nav-links">
    <li>Home</li><li>About us</li><li>Clients</li><li>Services</li><li>Careers</li><li>Contact us</li>
  </ul>
  <div class="nav-actions">
    <a class="pill-btn" href="#">Post job</a>
    <a class="pill-btn" href="#">Upload Resume</a>
  </div>
</nav>

<section class="hero">
  <div class="hero-photo" role="img" aria-label="Group photo of four smiling business team members"></div>
  <div class="hero-copy">
    <h1 class="hero-title">Delivering IT Excellence</h1>
    <p class="hero-text">Lorem ipsum dolor sit amet, dolore sapientem similique mei cu, no elitr aliquando quo, ius ad graeco legimus.</p>
  </div>
  <a class="hero-cta" href="#">Contact us
    <svg width="24" height="24" viewBox="0 0 24 24"><circle cx="12" cy="12" r="11" fill="#333"/><path d="M9.5 7l7 5-7 5z" fill="#ddd"/></svg>
  </a>
</section>

<section class="service-tabs">
  <div class="service-tab" style="width:282px">Packaged Applications</div>
  <div class="service-tab" style="width:262px">Enterprise Application<br>Integration</div>
  <div class="service-tab" style="width:213px">Digital Commerce</div>
  <div class="service-tab" style="width:333px">Application Development &amp;<br>Maintenance</div>
</section>

<section class="intro">
  <h2 class="intro-title">Welcome to Corvastin Office Solutions</h2>
  <p class="intro-sub">an emerging provider of global IT consulting and software services.</p>
  <p class="intro-text">Lorem ipsum dolor sit amet, dolore sapientem similique mei cu, no elitr aliquando quo, ius ad graeco legimus. Homero integre ex duo, cu mea quod cibo cotidieque, ea iuvaret erroribus cum. Te est audire meliore fabellas, nam ei bonorum nominati antiopam. His putant denique dissentiet ea. Option equidem sit ad, regione iudicabit usu te, liber utamur reprimique eos at. Semper iriure persequeris vis id, duo recteque forensibus deterruisset no, nec viderer commune no.</p>
  <p class="intro-text">Lorem ipsum dolor sit amet, dolore sapientem similique mei cu, no elitr aliquando quo, ius ad graeco legimus. Homero integre ex duo, cu mea quod cibo cotidieque, ea iuvaret erroribus cum. Te est audire meliore fabellas, nam ei bonorum nominati antiopam. His putant denique dissentiet ea. Option equidem sit ad, regione iudicabit usu te, liber utamur reprimique eos at. Semper iriure persequeris vis id, duo recteque forensibus deterruisset no, nec viderer commune no.</p>
</section>

<aside class="opportunities">
  <h2>Latest Opportunities</h2>
  <div class="job">
    Software Developers/Programmer<br>Analysts - AX<br>26/11/2013
    <div class="job-more">Read more &gt;&gt;</div>
  </div>
  <div class="job">
    Software Developers/Programmer<br>Analysts - AX<br>26/11/2013
    <div class="job-more">Read more &gt;&gt;</div>
  </div>
</aside>

<section class="clients">
  <h2>Clients</h2>
  <div class="client-row">
    <svg class="arrow arrow-prev" width="26" height="46" viewBox="0 0 26 46"><path d="M24 1L2 23l22 22" fill="none" stroke="#333" stroke-width="1.6"/></svg>
    <span class="client-name" style="left:202px">Brackwell's Wine</span>
    <span class="client-name" style="left:362px"><span class="client-mark" style="border-radius:50%"></span>Marlow Vines</span>
    <span class="client-name" style="left:525px">Ledger Cellar</span>
    <span class="client-name" style="left:725px">Kestrel Weinhaus</span>
    <span class="client-name" style="left:880px"><span class="client-mark"></span>Fennick Wine</span>
    <svg class="arrow arrow-next" width="26" height="46" viewBox="0 0 26 46"><path d="M2 1l22 22L2 45" fill="none" stroke="#333" stroke-width="1.6"/></svg>
  </div>
</section>

<footer class="site-footer">
  <nav class="footer-links">Home<span>|</span>About us<span>|</span>Clients<span>|</span>Services<span>|</span>Careers<span>|</span>Contact us</nav>
  <div class="social">
    <div class="social-btn"><span class="social-label"><i></i>Like</span><span class="social-count">56</span></div>
    <div class="social-btn"><span class="social-label"><i></i>Follow</span><span class="social-count">119</span></div>
  </div>
  <p class="copyright">Copyright 2014 Corvastin Office Solutions</p>
</footer>

</body>
</html>
```